Graphic Design Project

Hi Designers
New Label for New Rum .
The label we would like is it to be modern and smart looking, simple and eye catching. Ingenuity is required and a great open mind to creating this label. Type of rum -Rich flavour with a smooth rounded character. It has robust fruity flavours of molasses, honey and chocolate and is not as sweet as other rums, giving it a strong dark rum taste for the "real rum drinker. If you google Iron Tide Rum thats the type of bottle using .
Name is : Marrow Crest
Size:1l
Alcohol :37.5% Imported Dark Rum
Final designer will be paid extra for posters and t shirt designs. email is devran@tolvik.co.nz
Target Market(s)
Rum Drinkers .
Industry/Entity Type
Graphic Design

```html
<!DOCTYPE html>
<html lang="en">
<head>
<meta charset="utf-8">
<title>Marrow Crest Dark Rum – Label</title>
<link rel="stylesheet" href="https://fonts.googleapis.com/css2?family=Arvo:wght@700&family=Kaushan+Script&family=Mrs+Saint+Delafield&family=Rye&family=Yellowtail&display=swap">
<style>
  :root {
    --page: #ffffff;
    --bottle: #2e1a0e;
    --panel: #2a190c;
    --frame-gold: #d9a836;
    --frame-orange: #e08a1e;
    --base-brown: #3a2614;
    --title-gold: #d6b43a;
    --stamp-grey: #6e6158;
    --cream: #ffffff;
    --muted-brown: #6b5334;
    --dist-gold: #d9a72b;
  }
  * { margin: 0; padding: 0; box-sizing: border-box; }
  html, body { width: 1200px; height: 900px; overflow: hidden; background: var(--page); }
  .canvas { position: relative; width: 1200px; height: 900px; }

  .bottle { position: absolute; left: 0; top: 0; }

  .label {
    position: absolute;
    background: linear-gradient(to bottom, var(--frame-gold) 0%, #b88a35 45%, var(--base-brown) 100%);
    text-align: center;
  }
  .label__panel {
    position: absolute;
    background: var(--panel);
    border: solid var(--frame-orange);
  }
  .label__line { position: absolute; left: 0; right: 0; white-space: nowrap; }

  .stamp { font-family: "Rye", serif; color: var(--stamp-grey); letter-spacing: 0.04em; }
  .title { font-family: "Yellowtail", cursive; color: var(--title-gold); line-height: 1; }
  .kind { font-family: "Mrs Saint Delafield", cursive; color: var(--cream); }
  .notes { font-family: "Kaushan Script", cursive; color: var(--cream); }
  .spec { font-family: "Arvo", serif; font-weight: 700; color: var(--muted-brown); }
  .distributor { font-family: "Arvo", serif; font-weight: 700; color: var(--dist-gold); }

  /* Main label */
  .label--main { left: 499px; top: 82px; width: 574px; height: 753px; border-radius: 8px; }
  .label--main .label__panel { left: 19px; top: 21px; width: 536px; height: 672px; border-width: 5px; border-radius: 4px; }
  .label--main .stamp { top: 46px; font-size: 46px; }
  .label--main .title { font-size: 118px; }
  .label--main .title--one { top: 166px; }
  .label--main .title--two { top: 288px; left: 0; }
  .label--main .kind { top: 386px; left: 270px; right: auto; font-size: 52px; }
  .label--main .notes { font-size: 22px; }
  .label--main .notes--one { top: 486px; }
  .label--main .notes--two { top: 532px; left: -30px; }
  .label--main .notes--three { top: 572px; }
  .label--main .spec--vol { top: 618px; font-size: 18px; }
  .label--main .spec--abv { top: 646px; font-size: 13px; }
  .label--main .distributor--head { top: 702px; font-size: 15px; }
  .label--main .distributor--name { top: 722px; font-size: 13px; font-weight: 400; }

  /* Bottle label */
  .label--bottle { left: 118px; top: 403px; width: 220px; height: 377px; }
  .label--bottle .label__panel { left: 6px; top: 7px; width: 208px; height: 342px; border-width: 3px; }
  .label--bottle .stamp { top: 22px; font-size: 20px; }
  .label--bottle .title { font-size: 52px; }
  .label--bottle .title--one { top: 78px; }
  .label--bottle .title--two { top: 132px; left: -4px; }
  .label--bottle .kind { top: 190px; left: 112px; right: auto; font-size: 22px; }
  .label--bottle .notes { font-size: 9.5px; }
  .label--bottle .notes--one { top: 245px; }
  .label--bottle .notes--two { top: 266px; left: -12px; }
  .label--bottle .notes--three { top: 286px; }
  .label--bottle .spec--vol { top: 311px; font-size: 8px; }
  .label--bottle .spec--abv { top: 325px; font-size: 5.5px; }
  .label--bottle .distributor--head { top: 356px; font-size: 6.5px; }
  .label--bottle .distributor--name { top: 365px; font-size: 6px; font-weight: 400; }
</style>
</head>
<body>
<main class="canvas">
  <svg class="bottle" width="1200" height="900" viewBox="0 0 1200 900" role="img" aria-label="Dark rum bottle silhouette carrying the label">
    <path fill="var(--bottle)" d="M196,60 Q190,60 190,70 L190,95 L186,100 L186,180 Q186,250 140,300 Q118,325 118,360 L118,850 L338,850 L338,360 Q338,325 316,300 Q270,250 270,180 L270,100 L266,95 L266,70 Q266,60 260,60 Z"/>
  </svg>

  <section class="label label--bottle" aria-label="Bottle label">
    <div class="label__panel"></div>
    <p class="label__line stamp">IMPORTED</p>
    <p class="label__line title title--one">Marrow</p>
    <p class="label__line title title--two">Crest</p>
    <p class="label__line kind">Dark Rum</p>
    <p class="label__line notes notes--one">Robust fruity flavours of molasses infused</p>
    <p class="label__line notes notes--two">with honey and chocolate</p>
    <p class="label__line notes notes--three">and a smooth rounded character</p>
    <p class="label__line spec spec--vol">1 Litre</p>
    <p class="label__line spec spec--abv">37.5% Alcohol by Volume</p>
    <p class="label__line distributor distributor--head">Distributed by</p>
    <p class="label__line distributor distributor--name">??????????????????????????????????</p>
  </section>

  <section class="label label--main" aria-label="Flat label artwork">
    <div class="label__panel"></div>
    <p class="label__line stamp">IMPORTED</p>
    <p class="label__line title title--one">Marrow</p>
    <p class="label__line title title--two">Crest</p>
    <p class="label__line kind">Dark Rum</p>
    <p class="label__line notes notes--one">Robust fruity flavours of molasses infused</p>
    <p class="label__line notes notes--two">with honey and chocolate</p>
    <p class="label__line notes notes--three">and a smooth rounded character</p>
    <p class="label__line spec spec--vol">1 Litre</p>
    <p class="label__line spec spec--abv">37.5% Alcohol by Volume</p>
    <p class="label__line distributor distributor--head">Distributed by</p>
    <p class="label__line distributor distributor--name">???????????????????????????????????????</p>
  </section>
</main>
</body>
</html>
```